Backup Software Tri-fold Brochure Project

We need a great looking and informative brochure to describe our new Backup Software offering. The brochures are to be used in retail and small business environments given to clients interested in protecting their computer from data loss.
The brochure should include attractive imagery that conveys a sense of Trust and Security to the prospective client.
The copy is provided as an attachment to this project. We'd like our Steady Deskframe product logo to be printed on the back cover. The logo is attached to this project.
The finished tri-fold brochure will be submitted to Quellpress for printing as an 8.5" x 11" tri-fold brochure. Their design instructions are online http://quellpress-example.com/custom-brochures.aspx.
The finished product should be Adobe Illustrator CS3 (*.ai) with a PDF Proof.
Target Market(s)
Retail and Small Business customers
Industry/Entity Type
Software
Colors
Designer to choose colors to be used in the design.
Look and feel

```html
<!DOCTYPE html>
<html lang="en">
<head>
<meta charset="utf-8">
<title>Steady Deskframe – Tri-fold Brochure</title>
<link rel="stylesheet" href="https://fonts.googleapis.com/css2?family=Lato:wght@400;700;900&family=Oswald:wght@700&family=Montserrat:wght@300;500&display=swap">
<style>
  :root {
    --brand-blue: #1f5fa6;
    --brand-blue-deep: #164a86;
    --brand-blue-light: #3b86cf;
    --brand-green: #5cb83a;
    --ink: #2d2d2d;
    --ink-soft: #4a4a4a;
    --paper: #f6f6f6;
    --rule: #8a8a8a;
    --page-bg: #e4e4e4;
  }
  * { box-sizing: border-box; margin: 0; padding: 0; }
  html, body { width: 1200px; height: 764px; overflow: hidden; background: var(--page-bg); }
  .brochure { position: relative; width: 1200px; height: 764px; background: var(--paper); font-family: "Lato", sans-serif; overflow: hidden; }
  .artwork { position: absolute; inset: 0; }

  .intro-copy { position: absolute; left: 40px; top: 26px; width: 330px; color: #fff; }
  .section-title { font-family: "Lato", sans-serif; font-weight: 900; font-size: 15px; letter-spacing: 0.3px; text-transform: uppercase; margin-bottom: 10px; }
  .intro-copy p { font-size: 11.2px; line-height: 1.42; margin-bottom: 9px; }

  .detail-copy { position: absolute; left: 40px; top: 352px; width: 330px; color: var(--ink); }
  .detail-copy p { font-size: 11.5px; line-height: 1.45; }
  .detail-copy .rule { border: 0; border-top: 1.5px solid var(--rule); margin: 14px 0 16px; }
  .detail-copy .section-title { color: var(--brand-blue); font-size: 14px; margin-bottom: 6px; }
  .detail-copy .or-label { color: var(--brand-blue); font-weight: 900; font-size: 12px; margin: 4px 0; }

  .contact-block { position: absolute; left: 560px; top: 34px; width: 230px; color: #fff; }
  .contact-block .section-title { color: var(--brand-green); font-size: 13px; margin-bottom: 8px; }
  .contact-list { list-style: none; }
  .contact-list li { display: flex; align-items: flex-start; gap: 7px; font-size: 10.5px; line-height: 1.35; margin-bottom: 5px; }
  .contact-icon { flex: 0 0 13px; width: 13px; height: 13px; margin-top: 1px; }

  .brand-mark { display: flex; align-items: center; gap: 8px; font-family: "Lato", sans-serif; font-weight: 900; text-transform: uppercase; letter-spacing: 0.5px; }
  .brand-mark .brand-square { display: inline-block; background: currentColor; }
  .brand-mark--inside { position: absolute; left: 432px; top: 262px; color: #fff; font-size: 20px; }
  .brand-mark--inside .brand-square { width: 18px; height: 18px; }
  .brand-mark--cover { position: absolute; left: 860px; top: 548px; color: var(--brand-green); font-size: 25px; }
  .brand-mark--cover .brand-square { width: 22px; height: 22px; }

  .cover-tagline { position: absolute; left: 820px; top: 598px; width: 360px; text-align: center; line-height: 1; }
  .tagline-lead { display: block; font-family: "Montserrat", sans-serif; font-weight: 300; font-size: 30px; letter-spacing: 2px; color: var(--brand-blue); }
  .tagline-strong { display: block; font-family: "Oswald", sans-serif; font-weight: 700; font-size: 44px; color: var(--brand-green); margin: 4px 0; }
  .tagline-close { display: block; font-family: "Montserrat", sans-serif; font-weight: 500; font-size: 30px; letter-spacing: 2px; color: var(--ink); }
</style>
</head>
<body>
<main class="brochure">
  <svg class="artwork" width="1200" height="764" viewBox="0 0 1200 764" aria-hidden="false">
    <defs>
      <linearGradient id="panel-blue" x1="0" y1="0" x2="1" y2="1">
        <stop offset="0" stop-color="#164a86"/>
        <stop offset="1" stop-color="#2a72bf"/>
      </linearGradient>
      <linearGradient id="photo-tech" x1="0" y1="0" x2="1" y2="1">
        <stop offset="0" stop-color="#6f7f8e"/>
        <stop offset="0.5" stop-color="#b9c3cc"/>
        <stop offset="1" stop-color="#3f4a55"/>
      </linearGradient>
      <linearGradient id="photo-cloud" x1="0" y1="0" x2="0" y2="1">
        <stop offset="0" stop-color="#5d9ad6"/>
        <stop offset="1" stop-color="#2d68ad"/>
      </linearGradient>
    </defs>

    <!-- inside blue field -->
    <rect class="field-blue" x="0" y="0" width="800" height="764" fill="url(#panel-blue)"/>

    <!-- left panel white wave -->
    <path class="wave-white" d="M0,318 C130,278 290,286 400,356 C430,380 450,420 470,470 L470,764 H0 Z" fill="var(--paper)"/>

    <!-- middle lower photo -->
    <g role="img" aria-label="Blue-toned photo of a cloud icon connected to computers and devices">
      <path d="M400,764 V600 C430,520 470,490 530,474 C620,496 710,520 800,530 V764 Z" fill="url(#photo-cloud)"/>
    </g>

    <!-- photo right -->
    <g role="img" aria-label="Photo of a server room with a businessman's hand touching floating cloud and device icons">
      <path d="M530,470 C640,440 700,230 800,180 V0 H1200 V440 C1080,420 950,450 800,530 C700,520 610,496 530,470 Z" fill="url(#photo-tech)"/>
    </g>

    <!-- swoop lines -->
    <path d="M526,464 C636,434 696,224 800,174" fill="none" stroke="#fff" stroke-width="6"/>
    <path d="M520,470 C632,440 692,230 800,184" fill="none" stroke="var(--brand-green)" stroke-width="4"/>

    <!-- cover -->
    <path class="cover-white" d="M800,540 C950,462 1080,432 1200,452 V764 H800 Z" fill="var(--paper)"/>
    <path d="M800,526 C950,446 1080,418 1200,438" fill="none" stroke="var(--brand-blue)" stroke-width="16"/>

    <!-- fold lines -->
    <line x1="400" y1="0" x2="400" y2="764" stroke="#000" stroke-opacity="0.06"/>
    <line x1="800" y1="0" x2="800" y2="764" stroke="#000" stroke-opacity="0.06"/>
  </svg>

  <section class="intro-copy">
    <h2 class="section-title">We have what you need</h2>
    <p>We can create a snapshot of all the programs and files on your computer using our Image Backup technology. We'll give you a backup on an external hard drive which you keep in a safe place. If anything happens, just bring in your computer and your Image Backup and we'll restore your computer back to the point when the snapshot was taken.</p>
    <p>Restoring from an Image Backup is like setting your computer back in time. To make sure all your files and programs are safe, install Halvern-Net Steady Deskframe software. Nightly backups are stored in Halvern-Net's secure datacenter to protect you from even the most severe data loss scenarios.</p>
  </section>

  <section class="detail-copy">
    <p>The combination of your Image Backup and your nightly backup will ensure you have complete protection for both your programs and your files. It means complete peace of mind.</p>
    <hr class="rule">
    <h3 class="section-title">What to do</h3>
    <p>Call us to schedule a day to bring in your computer</p>
    <p class="or-label">OR</p>
    <p>Once a month we do "Image Backup Saturday". Drop off your computer in the morning and pick it up a few hours later. Call for a copy of our schedule.</p>
    <hr class="rule">
    <h3 class="section-title">Options</h3>
    <p>Our Image Backup technology can protect Panelix OS PC's and Laptops running Panelix OS 7 and above (Panelix OS 8, 10+). Panelix OS Servers running 2008 and above (2012, 2016+).</p>
  </section>

  <section class="contact-block">
    <h3 class="section-title">Contact us</h3>
    <ul class="contact-list">
      <li><svg class="contact-icon" viewBox="0 0 14 14"><circle cx="7" cy="7" r="7" fill="var(--brand-green)"/><path d="M7,3 a2.5,2.5 0 0 1 2.5,2.5 C9.5,7.5 7,11 7,11 C7,11 4.5,7.5 4.5,5.5 A2.5,2.5 0 0 1 7,3 Z" fill="#fff"/></svg>Lorem Ipsum is simply dummy text of the printing and typesetting</li>
      <li><svg class="contact-icon" viewBox="0 0 14 14"><circle cx="7" cy="7" r="7" fill="var(--brand-green)"/><path d="M4.5,3.5 L6,3.5 L6.6,5.5 L5.7,6.3 C6.2,7.4 6.8,8 7.8,8.5 L8.6,7.6 L10.5,8.2 L10.5,9.6 C7,10 4,7 4.5,3.5 Z" fill="#fff"/></svg>123-456-7890</li>
      <li><svg class="contact-icon" viewBox="0 0 14 14"><circle cx="7" cy="7" r="7" fill="var(--brand-green)"/><rect x="3.5" y="4.5" width="7" height="5" fill="none" stroke="#fff"/><path d="M3.5,4.5 L7,7.3 L10.5,4.5" fill="none" stroke="#fff"/></svg>youremail@mailbox-example.com</li>
      <li><svg class="contact-icon" viewBox="0 0 14 14"><circle cx="7" cy="7" r="7" fill="var(--brand-green)"/><circle cx="7" cy="7" r="3.6" fill="none" stroke="#fff"/><path d="M3.4,7 H10.6 M7,3.4 C5.4,5.5 5.4,8.5 7,10.6 C8.6,8.5 8.6,5.5 7,3.4" fill="none" stroke="#fff" stroke-width="0.8"/></svg>www.yourwebaddress.com</li>
    </ul>
  </section>

  <div class="brand-mark brand-mark--inside"><span class="brand-square"></span>Steady Deskframe</div>

  <div class="brand-mark brand-mark--cover"><span class="brand-square"></span>Steady Deskframe</div>

  <h1 class="cover-tagline">
    <span class="tagline-lead">THE ONLY</span>
    <span class="tagline-strong">PROTECTION IS A</span>
    <span class="tagline-close">GREAT BACKUP</span>
  </h1>
</main>
</body>
</html>
```